Real Estate Investing company needs a business card design

We need a business card design for new Real Estate Investment Company called "Maple Ridge Ventures, LLC." We buy homes for cash and close quickly in any situation. Our company provides an easy and fast option for home owners who are in tough situations who need to sell their home fast and don't want realtor fees or other listing hassles. We also renovate and resell our homes which helps provide housing for the community. We would like to see designs that use the colors blue and white to match our company logo or other colors that may match our company logo. The final design should communicate trust and easy process.
Industry/Entity Type
Business
Contact Information for Business Card
Front should have company name and company logo. back of card should have company logo and area to list services.
Look and feel

```html
<!DOCTYPE html>
<html lang="en">
<head>
<meta charset="utf-8">
<title>Maple Ridge Ventures – Business Card</title>
<link href="https://fonts.googleapis.com/css2?family=Open+Sans:wght@400;600;800&family=Roboto+Condensed:ital,wght@1,800&display=swap" rel="stylesheet">
<style>
  :root {
    --brand-blue: #0a72cc;
    --brand-blue-deep: #0660b2;
    --paper: #ffffff;
    --canvas: #e9ebee;
    --ink-light: #ffffff;
  }
  * { box-sizing: border-box; margin: 0; padding: 0; }
  html, body { width: 1200px; height: 960px; overflow: hidden; }
  body {
    background: var(--canvas);
    font-family: "Open Sans", Arial, sans-serif;
    display: flex;
    flex-direction: column;
    align-items: center;
    justify-content: center;
    gap: 56px;
  }
  .card {
    width: 660px;
    height: 377px;
    position: relative;
    overflow: hidden;
    box-shadow: 0 6px 18px rgba(0,0,0,0.18);
  }

  /* Front */
  .card-front {
    background: linear-gradient(135deg, var(--brand-blue) 0%, var(--brand-blue-deep) 100%);
    display: flex;
    align-items: center;
    justify-content: center;
  }
  .brand-name {
    font-family: "Open Sans", Arial, sans-serif;
    font-weight: 800;
    text-transform: uppercase;
    line-height: 1.05;
    text-align: center;
  }
  .card-front .brand-name {
    color: var(--ink-light);
    font-size: 46px;
    letter-spacing: 1px;
  }

  /* Back */
  .card-back { background: var(--paper); }
  .card-back .brand-name {
    position: absolute;
    top: 42px;
    left: 70px;
    color: var(--brand-blue);
    font-size: 34px;
    text-align: left;
  }
  .contact-band {
    position: absolute;
    left: 0;
    bottom: 0;
    width: 74%;
    height: 58%;
    background: var(--brand-blue);
    color: var(--ink-light);
    padding: 30px 34px;
    display: grid;
    grid-template-columns: 1fr 1fr;
    column-gap: 18px;
    font-size: 13px;
  }
  .contact-item {
    display: flex;
    align-items: flex-start;
    gap: 10px;
    margin-bottom: 16px;
    line-height: 1.45;
  }
  .contact-item svg { flex: none; width: 26px; height: 26px; }
  .contact-item b { font-weight: 600; }
  .contact-col-right { padding-top: 40px; }
  .tagline {
    position: absolute;
    right: 18px;
    bottom: 92px;
    width: 150px;
    font-family: "Roboto Condensed", "Arial Narrow", sans-serif;
    font-style: italic;
    font-weight: 800;
    font-size: 26px;
    line-height: 1.1;
    color: var(--brand-blue);
    text-align: center;
  }
</style>
</head>
<body>

  <section class="card card-front" aria-label="Business card front">
    <h1 class="brand-name">Maple Ridge<br>Ventures, LLC</h1>
  </section>

  <section class="card card-back" aria-label="Business card back">
    <h2 class="brand-name">Maple Ridge<br>Ventures, LLC</h2>

    <div class="contact-band">
      <div class="contact-col-left">
        <div class="contact-item">
          <svg viewBox="0 0 26 26" fill="none" stroke="#fff" stroke-width="2" stroke-linejoin="round"><path d="M3 13 L13 4 L23 13 M6 11 V22 H11 V16 H15 V22 H20 V11"/></svg>
          <span>Unit, Street<br>City, State, Zip Code</span>
        </div>
        <div class="contact-item">
          <svg viewBox="0 0 26 26" fill="none" stroke="#fff" stroke-width="2" stroke-linejoin="round"><path d="M8 3 L11 8 L9 10 C10 13 13 16 16 17 L18 15 L23 18 L21 22 C12 22 4 14 4 5 Z"/></svg>
          <span><b>T.</b> 555-014-0001<br><b>F.</b> 555-014-0002</span>
        </div>
      </div>
      <div class="contact-col-right">
        <div class="contact-item">
          <svg viewBox="0 0 26 26" fill="none" stroke="#fff" stroke-width="2" stroke-linejoin="round"><rect x="3" y="6" width="20" height="14"/><path d="M3 6 L13 14 L23 6"/></svg>
          <span>hello@mapleridgeventures.com</span>
        </div>
        <div class="contact-item">
          <svg viewBox="0 0 26 26" fill="none" stroke="#fff" stroke-width="1.8"><circle cx="13" cy="13" r="10"/><ellipse cx="13" cy="13" rx="4.5" ry="10"/><path d="M3 13 H23 M5 8 H21 M5 18 H21"/></svg>
          <span>www.mapleridgeventures.com</span>
        </div>
      </div>
    </div>

    <p class="tagline">Sell Your Home?</p>
  </section>

</body>
</html>
```